Natural, organic, vegan-friendly nutritious food supplements

We need packaging design for a new nutritious food supplement to be launched. The products are organic, natural, with no additives, lactose-free, gluten-free, vegan-friendly, etc. The product is a powder that comes in 40g sachets (need sachet design) which are then put into a box (need box design).

More details in the included zip file. Please do not hesitate to contact us for more information if needed.

Target Market(s)

Everyone interested in healthy food.

Requirements
Must have
• Vibrant colours, must be easy to read and easy to recognise on a shelf.
Natural colours.

```html
<!DOCTYPE html>
<html lang="en">
<head>
<meta charset="utf-8">
<title>SassyCocoBoom – Sketch sheet</title>
<link rel="stylesheet" href="https://fonts.googleapis.com/css2?family=Montserrat:wght@400;800&family=Libre+Baskerville&family=Roboto:wght@400&family=Kaushan+Script&display=swap">
<style>
  :root {
    --red: #a8232a;
    --band: #7a1a0e;
    --brown: #6b2a1e;
    --ink: #1d1d1d;
    --paper: #ffffff;
    --edge: #e6e6e6;
  }
  * { margin: 0; padding: 0; box-sizing: border-box; }
  html, body { width: 1200px; height: 746px; overflow: hidden; background: var(--paper); }
  .sheet { position: relative; width: 1200px; height: 746px; background: var(--paper); }

  .header-band { position: absolute; left: 0; top: 38px; }
  .header-title {
    position: absolute; left: 55px; top: 51px;
    font: 800 18px/1 "Montserrat", sans-serif; letter-spacing: 2.5px; color: var(--paper);
  }
  .header-title .light { font-weight: 400; }
  .header-script {
    position: absolute; left: 188px; top: 72px;
    font: 40px/1 "Kaushan Script", cursive; color: var(--band);
    transform: rotate(-6deg);
  }

  .variant-label {
    position: absolute; font: 800 17px/1 "Montserrat", sans-serif; color: var(--ink);
  }

  .sachet {
    position: absolute; width: 243px; height: 322px;
    background: var(--paper);
    box-shadow: 0 0 0 1px var(--edge), 0 4px 10px rgba(0,0,0,0.08);
  }
  .sachet-shape { position: absolute; inset: 0; }
  .brand-seal {
    position: absolute; left: 50%; top: 30px; width: 64px; height: 64px; margin-left: -32px;
    border: 1.5px solid var(--brown); border-radius: 50%;
    display: flex; align-items: center; justify-content: center;
    font: 800 13px/1 "Montserrat", sans-serif; letter-spacing: 1.5px; color: var(--brown);
  }
  .product-name {
    position: absolute; left: 0; right: 0; top: 101px; text-align: center;
    font: 800 11.5px/1 "Montserrat", sans-serif; letter-spacing: 2.4px; color: var(--brown);
  }
  .product-name .light { font-weight: 400; }
  .product-art {
    position: absolute; left: 52px; top: 124px; width: 140px; height: 106px;
    border-radius: 40% 45% 20% 20%;
    background: radial-gradient(circle at 40% 30%, #b98b63 0%, #6e3a22 55%, #3f1d10 100%);
  }
  .flavour {
    position: absolute; left: 57px; right: 57px; top: 248px; text-align: center;
    border-top: 1px solid var(--brown); border-bottom: 1px solid var(--brown);
    padding: 3px 0 2px;
    font: 12.5px/1.1 "Libre Baskerville", serif; color: var(--brown); white-space: nowrap;
  }
  .net-weight {
    position: absolute; right: 20px; top: 288px;
    font: 400 8px/1 "Roboto", sans-serif; color: var(--ink);
  }

  .brand-mark {
    position: absolute; left: 977px; top: 585px; width: 120px; height: 120px;
    border: 2px solid var(--ink); border-radius: 50%;
    display: flex; align-items: center; justify-content: center;
    font: 800 26px/1 "Montserrat", sans-serif; letter-spacing: 3px; color: var(--ink);
  }
</style>
</head>
<body>
<main class="sheet">

  <svg class="header-band" width="390" height="44" viewBox="0 0 390 44" aria-hidden="true">
    <polygon points="0,0 388,0 358,44 0,44" fill="var(--band)"/>
  </svg>
  <div class="header-title">SASSY<span class="light">COCO</span>BOOM</div>
  <div class="header-script">Sketch sheet</div>

  <!-- Variant 1 -->
  <section class="sachet" style="left:62px; top:203px;">
    <svg class="sachet-shape" viewBox="0 0 243 322" aria-hidden="true">
      <path d="M150,0 Q232,22 243,112 L243,0 Z" fill="var(--red)"/>
      <path d="M0,232 Q28,310 172,322 L0,322 Z" fill="var(--red)"/>
      <rect x="0" y="0" width="243" height="5" fill="var(--red)"/>
      <rect x="0" y="317" width="243" height="5" fill="var(--red)"/>
    </svg>
    <div class="brand-seal">PURA</div>
    <div class="product-name">SASSY<span class="light">COCO</span>BOOM</div>
    <div class="product-art" role="img" aria-label="Coconut halves splashing into melted chocolate with chocolate pieces"></div>
    <div class="flavour">Chocolate &amp; Coconut</div>
    <div class="net-weight">Net weight: 40g</div>
  </section>
  <div class="variant-label" style="left:182px; top:548px;">#1</div>

  <!-- Variant 2 -->
  <div class="variant-label" style="left:438px; top:240px;">#2</div>
  <section class="sachet" style="left:335px; top:262px;">
    <svg class="sachet-shape" viewBox="0 0 243 322" aria-hidden="true">
      <path d="M0,250 Q70,322 243,296 L243,322 L0,322 Z" fill="var(--red)"/>
      <rect x="0" y="316" width="243" height="6" fill="var(--red)"/>
    </svg>
    <div class="brand-seal">PURA</div>
    <div class="product-name">SASSY<span class="light">COCO</span>BOOM</div>
    <div class="product-art" role="img" aria-label="Coconut halves splashing into melted chocolate with chocolate pieces"></div>
    <div class="flavour">Chocolate &amp; Coconut</div>
    <div class="net-weight">Net weight: 40g</div>
  </section>

  <!-- Variant 3 -->
  <div class="variant-label" style="left:726px; top:184px;">#3</div>
  <section class="sachet" style="left:612px; top:203px;">
    <div class="brand-seal">PURA</div>
    <div class="product-name">SASSY<span class="light">COCO</span>BOOM</div>
    <div class="product-art" role="img" aria-label="Coconut halves splashing into melted chocolate with chocolate pieces"></div>
    <div class="flavour">Chocolate &amp; Coconut</div>
    <div class="net-weight">Net weight: 40g</div>
  </section>

  <!-- Variant 4 -->
  <div class="variant-label" style="left:1004px; top:127px;">#4</div>
  <section class="sachet" style="left:892px; top:146px;">
    <svg class="sachet-shape" viewBox="0 0 243 322" aria-hidden="true">
      <path d="M0,0 L243,0 L243,112 Q205,8 0,26 Z" fill="var(--red)"/>
    </svg>
    <div class="brand-seal">PURA</div>
    <div class="product-name">SASSY<span class="light">COCO</span>BOOM</div>
    <div class="product-art" role="img" aria-label="Coconut halves splashing into melted chocolate with chocolate pieces"></div>
    <div class="flavour">Chocolate &amp; Coconut</div>
    <div class="net-weight">Net weight: 40g</div>
  </section>

  <div class="brand-mark">PURA</div>

</main>
</body>
</html>
```